National wood flooring liquidator needs flyer

Need a flyer to provide house flippers, home builders, and home remodlers to call us on below wholesale wood flooring overstocks, dicontinues and one of a kinds that may be available in their area of the U.S. Availabilities in styles and quantities change daily and weekly and sell on 1st come basis.

Target Market(s)

house flippers, home builders, and home remodlers

Industry/Entity Type

Flooring

Number of Pages Required

1 page

Requirements
Must have
• Wood flooring only, 3/4" thick solid and engineered
Nice to have
• 4 color photos of wood flooring room scenes
Should not have
• No laminate, carpet or vinyl

```html
<!DOCTYPE html>
<html lang="en">
<head>
<meta charset="utf-8">
<title>Wholesale Wood Flooring Flyer</title>
<link href="https://fonts.googleapis.com/css2?family=Anton&family=Lato:wght@400;700&family=Libre+Baskerville:wght@700&family=Oswald:wght@300;500;700&display=swap" rel="stylesheet">
<style>
  :root {
    --page-bg: #e6e6e6;
    --panel-grey: #ececec;
    --white: #ffffff;
    --amber: #d9962e;
    --amber-light: #eaa94a;
    --amber-edge: #b8731c;
    --brown-dark: #3a1e0c;
    --brown-red: #6b2a10;
    --brand-brown: #a8660f;
    --charcoal: #2a2a2a;
    --ink: #1c1c1c;
    --body-ink: #333333;
  }
  * { box-sizing: border-box; margin: 0; padding: 0; }
  html, body { width: 1200px; height: 1166px; overflow: hidden; }
  body { background: var(--page-bg); position: relative; }

  .flyer {
    position: absolute; left: 196px; top: 23px;
    width: 808px; height: 1120px;
    background: var(--white);
    overflow: hidden;
    box-shadow: 0 2px 10px rgba(0,0,0,.15);
  }
  .flyer > * { position: absolute; }

  .intro-panel { left: 0; top: 0; width: 417px; height: 427px; background: var(--panel-grey); }

  .logo-box {
    left: 121px; top: 0; width: 188px; height: 188px;
    background: var(--white);
    border: 1.5px solid var(--amber-edge); border-top: none;
    display: flex; align-items: center; justify-content: center; text-align: center;
    font-family: "Oswald", sans-serif; font-weight: 500; font-size: 44px; line-height: 1.05;
    color: var(--ink);
  }

  .agency-name {
    left: 0; top: 240px; width: 417px; text-align: center;
    font-family: "Libre Baskerville", serif; font-weight: 700; font-size: 36px;
    color: var(--brand-brown); letter-spacing: .5px;
  }
  .agency-tagline {
    left: 0; top: 292px; width: 417px; text-align: center;
    font-family: "Oswald", sans-serif; font-weight: 300; font-size: 38px; line-height: 52px;
    color: var(--ink); letter-spacing: -.5px;
  }

  .hero-photo {
    left: 417px; top: 0; width: 391px; height: 680px;
    background: linear-gradient(160deg, #d7c7a4 0%, #a8895c 40%, #8a4f22 75%, #b8642a 100%);
  }
  .photo-rule { left: 417px; top: 680px; width: 391px; height: 8px; background: var(--charcoal); }

  .offer-band { left: 0; top: 427px; width: 417px; height: 270px; background: var(--amber); }
  .offer-lead {
    left: 0; top: 444px; width: 417px; text-align: center;
    font-family: "Lato", sans-serif; font-size: 23px; color: var(--white);
  }
  .offer-box {
    left: 8px; top: 484px; width: 396px; height: 213px;
    border: 2px solid var(--amber-edge); border-radius: 8px;
  }
  .offer-title {
    left: 8px; top: 486px; width: 396px; text-align: center;
    font-family: "Anton", sans-serif; font-size: 82px; line-height: 106px;
    color: var(--brown-dark); letter-spacing: 1px;
  }
  .offer-list {
    left: 8px; top: 590px; width: 396px; text-align: center;
    font-family: "Oswald", sans-serif; font-weight: 500; font-size: 20px;
    color: var(--brown-red);
  }
  .offer-note {
    left: 8px; top: 623px; width: 396px; text-align: center;
    font-family: "Oswald", sans-serif; font-weight: 700; font-size: 23px; line-height: 30px;
    color: var(--white); letter-spacing: .3px;
  }

  .history-bar { left: 0; top: 718px; width: 460px; height: 50px; }
  .history-text {
    left: 30px; top: 718px; height: 50px; line-height: 50px;
    font-family: "Lato", sans-serif; font-size: 22px; color: var(--white);
  }

  .body-copy {
    left: 477px; top: 722px; width: 304px;
    font-family: "Lato", sans-serif; font-size: 11.5px; line-height: 14px;
    color: var(--body-ink); text-align: justify;
  }

  .client-photo {
    left: 83px; top: 773px; width: 211px; height: 241px;
    background: linear-gradient(180deg, #d9b49a 0%, #9ab3cf 55%, #c9c9c9 100%);
  }

  .thumb { top: 835px; width: 212px; height: 155px; background: var(--charcoal); padding: 8px; }
  .thumb-kitchen { left: 352px; }
  .thumb-bath { left: 573px; }
  .thumb-fill { width: 100%; height: 100%; }
  .thumb-kitchen .thumb-fill { background: linear-gradient(180deg, #8a5a2e 0%, #b07a40 55%, #9a6330 100%); }
  .thumb-bath .thumb-fill { background: linear-gradient(180deg, #b0553a 0%, #c9c2b8 55%, #c08a5a 100%); }

  .footer-amber { left: 410px; top: 1021px; width: 398px; height: 99px; background: var(--amber); border-top: 6px solid var(--amber-light); }
  .footer-dark { left: 0; top: 1012px; width: 500px; height: 108px; }

  .contact-line {
    left: 30px; display: flex; align-items: center; gap: 22px;
    font-family: "Lato", sans-serif; font-size: 19px; color: var(--white);
  }
  .contact-email { top: 1028px; }
  .contact-web { top: 1058px; font-size: 21px; }
  .contact-line svg { width: 24px; height: 24px; flex: none; }

  .phone {
    left: 488px; top: 1038px; display: flex; align-items: center; gap: 12px;
    font-family: "Lato", sans-serif; font-weight: 700; font-size: 37px; color: var(--white);
  }
  .phone svg { width: 44px; height: 44px; }
</style>
</head>
<body>
<main class="flyer">
  <div class="intro-panel"></div>
  <div class="logo-box">Your<br>LOGO</div>

  <h1 class="agency-name">LOREM IPSUM</h1>
  <p class="agency-tagline">Liquidators specializing in<br>real wood flooring</p>

  <div class="hero-photo" role="img" aria-label="Dining room with solid hardwood floor, wooden table and chairs"></div>
  <div class="photo-rule"></div>

  <div class="offer-band"></div>
  <p class="offer-lead">3/4" solid &amp; engineered wood</p>
  <div class="offer-box"></div>
  <h2 class="offer-title">Wholesale</h2>
  <p class="offer-list">• overstocks • discontinued • one of a kinds</p>
  <p class="offer-note">1st come basis as all styles and<br>quantities change daily and weekly.</p>

  <svg class="history-bar" viewBox="0 0 460 50" aria-hidden="true">
    <polygon points="0,0 410,0 410,-20 460,-20 460,50 0,50" fill="var(--charcoal)"/>
  </svg>
  <p class="history-text">For flippers, builders &amp; remodelers</p>

  <p class="body-copy">We liquidate wholesale 3/4" solid and engineered wood flooring nationwide: overstocks, discontinued lines and one of a kind lots that may be near your area of the U.S. No laminate, carpet or vinyl, only real hardwood priced below wholesale. Call us today to hear what is in stock.</p>

  <div class="client-photo" role="img" aria-label="Excited customer at a laptop"></div>

  <div class="thumb thumb-kitchen"><div class="thumb-fill" role="img" aria-label="Kitchen with wood flooring"></div></div>
  <div class="thumb thumb-bath"><div class="thumb-fill" role="img" aria-label="Bathroom with brick wall and wood flooring"></div></div>

  <div class="footer-amber"></div>
  <svg class="footer-dark" viewBox="0 0 500 108" aria-hidden="true">
    <polygon points="0,0 396,0 497,108 0,108" fill="var(--charcoal)"/>
  </svg>

  <p class="contact-line contact-email">
    <svg viewBox="0 0 24 24" aria-hidden="true"><rect x="2" y="5" width="20" height="14" fill="none" stroke="#fff" stroke-width="1.5"/><polyline points="2,5 12,13 22,5" fill="none" stroke="#fff" stroke-width="1.5"/></svg>
    LOREM@lorem ipsum.com
  </p>
  <p class="contact-line contact-web">
    <svg viewBox="0 0 24 24" aria-hidden="true"><circle cx="12" cy="12" r="10" fill="none" stroke="#fff" stroke-width="1.5"/><ellipse cx="12" cy="12" rx="4.5" ry="10" fill="none" stroke="#fff" stroke-width="1.5"/><line x1="2" y1="12" x2="22" y2="12" stroke="#fff" stroke-width="1.5"/><line x1="4" y1="7" x2="20" y2="7" stroke="#fff" stroke-width="1.2"/><line x1="4" y1="17" x2="20" y2="17" stroke="#fff" stroke-width="1.2"/></svg>
    www.lorem ipsum.com.au
  </p>

  <p class="phone">
    <svg viewBox="0 0 44 44" aria-hidden="true"><circle cx="22" cy="22" r="20" fill="none" stroke="#fff" stroke-width="2.5"/><path d="M15 12 l5 -1 l3 7 l-3 2 c1.5 3.5 3.5 5.5 7 7 l2 -3 l7 3 l-1 5 c-9 1 -21 -11 -20 -20 z" fill="none" stroke="#fff" stroke-width="2.2" stroke-linejoin="round"/></svg>
    000 0000 000
  </p>
</main>
</body>
</html>
```